Hi Marlow,

I would like you to design for me a menu board for all my products.

The layout I have hand drawn for you so just follow my layout.

Pho
Noodle salads
Rice
StirFry with Thick Rice Noodles
Spring Rolls Ricepaper Rolls

Poster Size: AO Vertical ( 841W x 1189H)

There are more photos of the rice dishes but I thought I can send this through so you can start and I can send you the rest of the photos when I get back from my photographer.

I will have items descriptions to follow also

Requirements
Must have

```html
<!DOCTYPE html>
<html lang="en">
<head>
<meta charset="utf-8">
<title>Menu Board</title>
<link rel="stylesheet" href="https://fonts.googleapis.com/css2?family=Cinzel:wght@600&family=Jost:wght@500&display=swap">
<style>
  :root {
    --page: #ececea;
    --board-light: #3d3d3d;
    --board-dark: #1b1b1b;
    --chalk: #f4f4f2;
    --dash: rgba(244, 244, 242, 0.75);
    --dash-soft: rgba(244, 244, 242, 0.35);
    --plate: #ffffff;
    --broth: #8a5a32;
    --greens: #4f8a3a;
    --carrot: #e0782c;
    --rice: #f1e6cf;
  }
  * { box-sizing: border-box; margin: 0; padding: 0; }
  html, body {
    width: 1200px;
    height: 2225px;
    overflow: hidden;
    background: var(--page);
  }
  .menu-board {
    position: absolute;
    left: 50px;
    top: 341px;
    width: 1100px;
    height: 1542px;
    background:
      repeating-linear-gradient(90deg, rgba(255,255,255,0.018) 0 2px, transparent 2px 92px),
      radial-gradient(ellipse at 50% 35%, var(--board-light), var(--board-dark) 85%);
    box-shadow: 0 10px 30px rgba(0,0,0,0.25);
  }
  .board-frame {
    position: absolute;
    inset: 26px;
    border: 3px dashed var(--dash);
    border-radius: 50px;
  }
  .menu-title {
    position: absolute;
    top: 40px;
    width: 100%;
    text-align: center;
    font-family: "Cinzel", serif;
    font-weight: 600;
    font-size: 64px;
    letter-spacing: 2px;
    color: var(--chalk);
  }
  .dish-row {
    position: absolute;
    left: 0;
    width: 100%;
    display: flex;
    justify-content: center;
  }
  .dish {
    display: flex;
    flex-direction: column;
    align-items: center;
    text-align: center;
    width: 262px;
  }
  .dish-row--soups .dish { width: 273px; }
  .dish-row--soups .dish + .dish,
  .dish-row--grid .dish + .dish {
    border-left: 3px dashed var(--dash-soft);
  }
  .dish-name {
    font-family: "Jost", sans-serif;
    font-weight: 500;
    font-size: 23px;
    line-height: 28px;
    text-transform: uppercase;
    color: var(--chalk);
    margin-top: 18px;
  }
  .bowl-photo {
    width: 232px;
    height: 145px;
    border-radius: 50% 50% 48% 48% / 30% 30% 70% 70%;
    border: 8px solid var(--plate);
    border-top-width: 4px;
    background: radial-gradient(ellipse at 50% 30%, var(--carrot) 0 18%, var(--greens) 30%, var(--broth) 60%, var(--plate) 62%);
  }
  .plate-photo {
    width: 200px;
    height: 200px;
    border-radius: 50%;
    border: 6px solid var(--plate);
    background: radial-gradient(circle at 45% 45%, var(--carrot) 0 15%, var(--greens) 35%, #8b6a4a 65%, var(--plate) 100%);
  }
  .plate-photo--rice { background: radial-gradient(circle at 50% 50%, var(--carrot) 0 10%, var(--rice) 40%, var(--plate) 100%); }
  .plate-photo--rolls { background: radial-gradient(circle at 50% 55%, var(--rice) 0 35%, #cde0b4 55%, var(--plate) 90%); }
  .row-1 { top: 140px; }
  .row-2 { top: 395px; }
  .row-3 { top: 612px; }
  .row-4 { top: 922px; }
  .row-5 { top: 1234px; }
</style>
</head>
<body>
  <main class="menu-board">
    <div class="board-frame"></div>
    <h1 class="menu-title">MENU</h1>

    <section class="dish-row dish-row--soups row-1">
      <div class="dish"><div class="bowl-photo" role="img" aria-label="Bowl of beef pho"></div><p class="dish-name">Beef Pho</p></div>
      <div class="dish"><div class="bowl-photo" role="img" aria-label="Bowl of chicken pho"></div><p class="dish-name">Chicken Pho</p></div>
      <div class="dish"><div class="bowl-photo" role="img" aria-label="Bowl of tofu pho"></div><p class="dish-name">Tofu Pho</p></div>
    </section>

    <section class="dish-row dish-row--grid row-2">
      <div class="dish"><div class="bowl-photo" role="img" aria-label="Bowl of beef pho"></div><p class="dish-name">Beef Pho</p></div>
      <div class="dish"><div class="bowl-photo" role="img" aria-label="Bowl of chicken pho"></div><p class="dish-name">Chicken Pho</p></div>
      <div class="dish"><div class="bowl-photo" role="img" aria-label="Bowl of BBQ pork noodle"></div><p class="dish-name">BBQ Pork Noodle</p></div>
      <div class="dish"><div class="bowl-photo" role="img" aria-label="Bowl of beef pho"></div><p class="dish-name">Beef Pho</p></div>
    </section>

    <section class="dish-row dish-row--grid row-3">
      <div class="dish"><div class="plate-photo" role="img" aria-label="Stir fry rice noodles with beef"></div><p class="dish-name">Stir Fry Rice<br>Noodles Beef</p></div>
      <div class="dish"><div class="plate-photo" role="img" aria-label="Stir fry rice noodles with chicken"></div><p class="dish-name">Stir Fry Rice<br>Noodles Chicken</p></div>
      <div class="dish"><div class="plate-photo" role="img" aria-label="Tofu with rice"></div><p class="dish-name">Tofu W Rice</p></div>
      <div class="dish"><div class="plate-photo plate-photo--rice" role="img" aria-label="Fried rice"></div><p class="dish-name">Fried Rice</p></div>
    </section>

    <section class="dish-row dish-row--grid row-4">
      <div class="dish"><div class="plate-photo" role="img" aria-label="Stir fry rice noodles with beef"></div><p class="dish-name">Stir Fry Rice<br>Noodles Beef</p></div>
      <div class="dish"><div class="plate-photo" role="img" aria-label="Stir fry rice noodles with chicken"></div><p class="dish-name">Stir Fry Rice<br>Noodles Chicken</p></div>
      <div class="dish"><div class="plate-photo" role="img" aria-label="Tofu with rice"></div><p class="dish-name">Tofu W Rice</p></div>
      <div class="dish"><div class="plate-photo plate-photo--rice" role="img" aria-label="Fried rice"></div><p class="dish-name">Fried Rice</p></div>
    </section>

    <section class="dish-row row-5">
      <div class="dish"><div class="plate-photo" role="img" aria-label="Lemongrass chilli chicken with rice"></div><p class="dish-name">Lemongrass Chilli<br>Chicken W Rice</p></div>
      <div class="dish"><div class="plate-photo plate-photo--rolls" role="img" aria-label="Ricepaper rolls"></div><p class="dish-name">Ricepaper Rolls</p></div>
    </section>
  </main>
</body>
</html>
```